Text design/overlay needed for promotional music release cover photo

I need the following text elements added to the attached image:
Element 1: Brent Colfax and The Kinship Circle
Element 2. This all needs to be clear and prominent : Featuring: Warren Petty, Corey Halvin, Renata Bloor, Ingrid Palumbo, Martin "Chipper" Lowe, Tamara Ridgely, Wa Ni Po Glen Harker, Nolan Brackett, Otis Crane, Dustin Pell, and The Final Grooveling
Element 3 ("WILLOW BEND" needs to pop): New single WILLOW BEND available everywhere 9/26
The final image needs to be 16:9 ratio. Colors should be black and samples from the bench in the image. Various fonts, text sizes, etc. The music is a reggae/bluegrass blend. I'm looking for art not AI. Thanks!

```html
<!DOCTYPE html>
<html lang="en">
<head>
<meta charset="utf-8">
<title>Brent Colfax and The Kinship Circle – Willow Bend</title>
<link rel="stylesheet" href="https://fonts.googleapis.com/css2?family=Anton&family=Archivo:wght@700;800&family=Open+Sans:wdth,wght@75..100,400..800&family=Rubik+Dirt&display=swap">
<style>
  :root {
    --ink: #231f20;
    --sun: #f7e04a;
    --outline: #f5e45c;
    --flag-red: #e8291c;
    --bone: #efe9dc;
    --leaf: #5f9e24;
    --leaf-deep: #2f6a1a;
    --bench-orange: #f06a12;
    --white: #ffffff;
  }
  * { margin: 0; padding: 0; box-sizing: border-box; }
  html, body { width: 1200px; height: 675px; overflow: hidden; background: #fff; }
  .cover { position: relative; width: 1200px; height: 675px; overflow: hidden; }

  .cover-photo {
    position: absolute; inset: 0;
    background:
      radial-gradient(ellipse 170px 120px at 160px 610px, rgba(240,60,30,.75), transparent 70%),
      radial-gradient(ellipse 220px 150px at 40px 560px, rgba(240,225,60,.8), transparent 70%),
      radial-gradient(ellipse 330px 220px at 1090px 560px, rgba(120,200,60,.85), transparent 70%),
      radial-gradient(ellipse 200px 130px at 920px 440px, rgba(200,225,70,.6), transparent 70%),
      radial-gradient(ellipse 260px 200px at 620px 560px, rgba(175,165,150,.9), transparent 75%),
      linear-gradient(180deg, #eef3ee 0%, #d9ead0 12%, #7fb43e 30%, #6aa32c 55%, #8ea05c 75%, #9c9486 100%);
  }

  .headline { position: absolute; left: 0; top: 0; width: 1200px; height: 675px; }
  .headline-name {
    font-family: "Anton", "Impact", sans-serif;
    fill: var(--ink);
    stroke: var(--outline);
    stroke-width: 4;
    paint-order: stroke;
  }

  .single-tag {
    position: absolute; left: 60px; top: 389px; width: 166px; height: 25px;
    background: var(--flag-red);
    color: var(--white);
    font-family: "Archivo", "Arial", sans-serif; font-weight: 800;
    font-size: 19px; letter-spacing: -0.5px; line-height: 25px; text-align: center;
  }
  .single-title {
    position: absolute; left: 42px; top: 418px; width: 335px; height: 124px;
    background: #141213;
    transform: rotate(-1.5deg);
    display: flex; align-items: center; justify-content: center;
    color: var(--bone);
    font-family: "Rubik Dirt", "Impact", sans-serif;
    font-size: 47px; letter-spacing: -1px; line-height: 1;
  }

  .band-name {
    position: absolute; left: 708px; top: 431px; width: 380px; height: 68px;
    background: linear-gradient(90deg, var(--leaf-deep) 0%, var(--leaf) 18%, var(--bench-orange) 55%, var(--leaf) 85%, var(--leaf-deep) 100%);
    display: flex; align-items: center; justify-content: center;
    color: #0c0a0a;
    font-family: "Anton", "Impact", sans-serif;
    font-size: 36px; line-height: 1;
  }

  .release { position: absolute; left: 556px; top: 514px; width: 600px; height: 56px; }
  .release-text { font-family: "Anton", "Impact", sans-serif; fill: var(--sun); }

  .featuring-label {
    position: absolute; left: 586px; top: 578px;
    color: var(--white);
    font-family: "Open Sans", "Arial", sans-serif; font-weight: 700;
    font-size: 24px; letter-spacing: 10px; line-height: 30px;
  }
  .featuring-list {
    position: absolute; left: 830px; top: 575px; width: 340px;
    color: var(--white);
    font-family: "Open Sans", "Arial", sans-serif; font-weight: 700; font-stretch: 75%;
    font-size: 13px; line-height: 19px; text-align: center; text-transform: uppercase;
    text-shadow: 0 0 3px rgba(0,0,0,.35);
    list-style: none;
  }
</style>
</head>
<body>
<main class="cover">
  <div class="cover-photo" role="img" aria-label="Photo: a bearded musician in a cap and sunglasses lounging on a striped green, yellow, orange and red bench beside an electric guitar, on a gravel road through sunny green woods, with drifts of yellow, red and green smoke"></div>

  <svg class="headline" viewBox="0 0 1200 675" aria-label="Brent Colfax">
    <text class="headline-name" x="115" y="405" font-size="430" textLength="965" lengthAdjust="spacingAndGlyphs">BRENT COLFAX</text>
  </svg>

  <div class="single-tag">NEW SINGLE!</div>
  <div class="single-title">WILLOW BEND</div>

  <div class="band-name">AND THE KINSHIP CIRCLE</div>

  <svg class="release" viewBox="0 0 600 56" aria-label="Available everywhere 9/26">
    <text class="release-text" x="0" y="52" font-size="58" textLength="596" lengthAdjust="spacingAndGlyphs">AVAILABLE EVERYWHERE 9/26</text>
  </svg>

  <div class="featuring-label">FEATURING:</div>
  <ul class="featuring-list">
    <li>Warren Petty, Corey Halvin, Renata Bloor,</li>
    <li>Ingrid Palumbo, Martin "Chipper" Lowe, Tamara Ridgely,</li>
    <li>Wa Ni Po Glen Harker, Nolan Brackett, Otis Crane,</li>
    <li>Dustin Pell, and The Final Grooveling</li>
  </ul>
</main>
</body>
</html>
```